Carry The Tide Home

Business Card design

Target Market(s)

People who require support in the commnity

Industry/Entity Type

Mental Health Support

Contact Information for Business Card

Mental Health Support Rosalind Bratten carrythetidehome@mailvane.com.au 0481 637 592 PO Box 629 Coolwater Bay QLD 4571

Colors
6B429C
8869AF
B7A5CE
E3DAEB
F3F0F8

Requirements
Must have
• Logo & details listed above
Should not have
• No red or orange

```html
<!DOCTYPE html>
<html lang="en">
<head>
<meta charset="utf-8">
<title>Carry The Tide Home — Business Card</title>
<link rel="stylesheet" href="https://fonts.googleapis.com/css2?family=Lato:wght@400;700;900&display=swap">
<style>
  :root {
    --stage: #2b2b2e;
    --card: #6b429c;
    --violet-mid: #8869af;
    --violet-soft: #b7a5ce;
    --lilac: #e3daeb;
    --mist: #f3f0f8;
    --ink-white: #ffffff;
  }
  * { box-sizing: border-box; margin: 0; padding: 0; }
  html, body {
    width: 1200px; height: 875px; overflow: hidden;
    background: var(--stage);
    font-family: "Lato", sans-serif;
  }
  .canvas {
    width: 1200px; height: 875px;
    display: flex; align-items: center; justify-content: center; gap: 44px;
  }
  .card {
    position: relative;
    width: 540px; height: 310px;
    background: var(--card);
    border-radius: 22px;
    overflow: hidden;
  }
  /* Front */
  .card--front { display: flex; align-items: center; justify-content: center; }
  .brand { display: flex; align-items: center; gap: 12px; }
  .brand__dot {
    width: 12px; height: 12px; border-radius: 50%;
    background: var(--lilac);
  }
  .brand__name {
    font-weight: 700; font-size: 26px; letter-spacing: 0.16em;
    text-transform: uppercase; color: var(--lilac);
  }
  /* Back */
  .card__feature {
    position: absolute; top: -60px; right: -60px;
    width: 420px; height: 360px;
    background: radial-gradient(closest-side at 58% 48%, var(--violet-soft) 0%, var(--violet-mid) 40%, rgba(136,105,175,0) 100%);
  }
  .details {
    position: absolute; left: 34px; bottom: 30px;
    color: var(--ink-white);
  }
  .details__name {
    font-weight: 900; font-size: 30px; text-transform: uppercase;
    letter-spacing: 0.01em; line-height: 1;
  }
  .details__role {
    font-weight: 400; font-size: 17px; margin-top: 4px; color: var(--mist);
  }
  .details__list { list-style: none; margin-top: 12px; }
  .details__item {
    display: flex; align-items: center; gap: 12px;
    font-size: 14px; line-height: 1.55; color: var(--mist);
  }
  .details__item--phone { font-size: 22px; line-height: 1.3; color: var(--ink-white); }
  .details__icon { width: 14px; height: 14px; flex: none; fill: var(--ink-white); }
</style>
</head>
<body>
<main class="canvas">
  <section class="card card--front" aria-label="Card front">
    <div class="brand">
      <span class="brand__dot"></span>
      <span class="brand__name">Carry The Tide Home</span>
    </div>
  </section>

  <section class="card card--back" aria-label="Card back">
    <div class="card__feature" role="img" aria-label="Soft violet glow where the brand emblem sits"></div>
    <div class="details">
      <h1 class="details__name">Rosalind Bratten</h1>
      <p class="details__role">Mental Health Support</p>
      <ul class="details__list">
        <li class="details__item details__item--phone">
          <svg class="details__icon" viewBox="0 0 24 24" aria-hidden="true"><path d="M6.6 10.8a15.1 15.1 0 0 0 6.6 6.6l2.2-2.2c.3-.3.7-.4 1-.2 1.1.4 2.3.6 3.6.6.6 0 1 .4 1 1V20c0 .6-.4 1-1 1A17 17 0 0 1 3 4c0-.6.4-1 1-1h3.5c.6 0 1 .4 1 1 0 1.3.2 2.5.6 3.6.1.3 0 .7-.2 1z"/></svg>
          0481 637 592
        </li>
        <li class="details__item">
          <svg class="details__icon" viewBox="0 0 24 24" aria-hidden="true"><path d="M2 5h20v14H2zM4 7v.5l8 5 8-5V7z"/></svg>
          carrythetidehome@mailvane.com.au
        </li>
        <li class="details__item">
          <svg class="details__icon" viewBox="0 0 24 24" aria-hidden="true"><path d="M12 2a7 7 0 0 0-7 7c0 5.2 7 13 7 13s7-7.8 7-13a7 7 0 0 0-7-7zm0 9.5A2.5 2.5 0 1 1 12 6.5a2.5 2.5 0 0 1 0 5z"/></svg>
          PO Box 629 Coolwater Bay QLD 4571
        </li>
      </ul>
    </div>
  </section>
</main>
</body>
</html>
```